Upscale business cards needed for Board of Directors

We need professional business cards created for members of our family business Board of Directors. We would like these relatively simple and straightforward, but also with a unique element to set them apart. Probably stick with neutral and simple colors - white, grey etc. We need space for the traditional elements, including name, title, address, email/phone number. And we will be creating several from this template so it needs to be template that is easy to switch information in and out of.
Business
See description

```html
<!DOCTYPE html>
<html lang="en">
<head>
<meta charset="utf-8">
<title>Harborline Holdings – Business Cards</title>
<link href="https://fonts.googleapis.com/css2?family=Source+Sans+3:wght@400;600;700&display=swap" rel="stylesheet">
<style>
  :root {
    --backdrop: #3b3b3b;
    --card: #2d2c2c;
    --ink-light: #ffffff;
    --ink-muted: #9a9a9a;
    --ink-soft: #b4b4b4;
    --accent: #b7a47e;
    --divider: #4a4848;
  }
  * { margin: 0; padding: 0; box-sizing: border-box; }
  html, body {
    width: 1200px;
    height: 1000px;
    overflow: hidden;
    background: var(--backdrop);
    font-family: "Source Sans 3", sans-serif;
  }
  .canvas { position: relative; width: 1200px; height: 1000px; }
  .card {
    position: absolute;
    left: 287px;
    width: 626px;
    height: 358px;
    background: var(--card);
  }
  .card--front { top: 140px; }
  .card--back { top: 531px; }

  .wordmark {
    position: absolute;
    color: var(--ink-light);
    font-weight: 700;
    text-align: center;
    line-height: 1;
  }
  .wordmark__primary { display: block; letter-spacing: 0.01em; }
  .wordmark__secondary { display: block; letter-spacing: 0.28em; }

  .card--front .wordmark { left: 0; right: 0; top: 140px; }
  .card--front .wordmark__primary { font-size: 60px; }
  .card--front .wordmark__secondary { font-size: 30px; margin-top: 14px; padding-left: 0.28em; }

  .website {
    position: absolute;
    left: 0; right: 0; top: 308px;
    text-align: center;
    color: var(--ink-muted);
    font-size: 14px;
  }

  .card--back .wordmark { left: 24px; width: 330px; top: 146px; }
  .card--back .wordmark__primary { font-size: 36px; }
  .card--back .wordmark__secondary { font-size: 18px; margin-top: 8px; padding-left: 0.28em; }

  .card__divider {
    position: absolute;
    left: 313px; top: 112px;
    width: 1px; height: 134px;
    background: var(--divider);
  }
  .contact {
    position: absolute;
    left: 338px; top: 106px;
    color: var(--ink-soft);
    font-size: 14px;
    line-height: 18px;
  }
  .contact__name { color: var(--accent); font-size: 18px; font-weight: 700; line-height: 22px; }
  .contact__title { margin-bottom: 10px; }
  .contact__row { display: flex; }
  .contact__label { color: var(--accent); width: 14px; }
  .contact__sep { width: 12px; }
  .contact__address { margin-top: 9px; }
</style>
</head>
<body>
<main class="canvas">
  <section class="card card--front" aria-label="Card front">
    <div class="wordmark">
      <span class="wordmark__primary">HARBORLINE</span>
      <span class="wordmark__secondary">HOLDINGS</span>
    </div>
    <p class="website">www.harborlineholdings.com</p>
  </section>

  <section class="card card--back" aria-label="Card back">
    <div class="wordmark">
      <span class="wordmark__primary">HARBORLINE</span>
      <span class="wordmark__secondary">HOLDINGS</span>
    </div>
    <div class="card__divider"></div>
    <div class="contact">
      <p class="contact__name">Daniel Reeves</p>
      <p class="contact__title">President</p>
      <p class="contact__row"><span class="contact__label">P</span><span class="contact__sep">:</span>012-555-0148</p>
      <p class="contact__row"><span class="contact__label">E</span><span class="contact__sep">:</span>info@harborlineholdings.com</p>
      <p class="contact__row"><span class="contact__label">W</span><span class="contact__sep">:</span>www.harborlineholdings.com</p>
      <p class="contact__address">Street name, Suite 100 State,<br>Zip Code, Country</p>
    </div>
  </section>
</main>
</body>
</html>
```